TIDAL VERGE needs bisness cards pronto

Bisness name is "TIDAL VERGE" new bisness the bisness includes lawn mowing, garden matanace, and any jobs around the house.
I need a card that is colorful and vibrant and the bisness of lawn mowing maybe with some nature with it. It also needs my contact details"Darren Quellby mobile 0413562049 call for free quote and email norma.vance@fernmail.com.au and a catchy tag line

Industry/Entity Type

House

Requirements
Must have
• Bisness name "TIDAL VERGE"
Contact details "0413562049"
Email norma.vance@fernmail.com.au
Call for free quote

```html
<!DOCTYPE html>
<html lang="en">
<head>
<meta charset="utf-8">
<title>Tidal Verge — Business Cards</title>
<link rel="stylesheet" href="https://fonts.googleapis.com/css2?family=Oswald:wght@500;700&display=swap">
<style>
  :root {
    --backdrop: #d9d9d6;
    --card-black: #0b0b0b;
    --brand-red: #e2323a;
    --brand-green: #8cc63f;
    --grass-light: #4fb52c;
    --grass-dark: #1f6b14;
    --laser-blue: #3b4fd6;
    --photo-tone-a: #5a93c4;
    --photo-tone-b: #4c8a9a;
  }
  * { box-sizing: border-box; margin: 0; padding: 0; }
  html, body {
    width: 1200px; height: 900px; overflow: hidden;
    background: var(--backdrop);
    font-family: "Oswald", "Arial Narrow", sans-serif;
  }
  .sheet {
    width: 1200px; height: 900px;
    display: flex; align-items: center; justify-content: center; gap: 40px;
  }
  .card {
    position: relative; width: 540px; height: 328px;
    background: var(--card-black); overflow: hidden;
    box-shadow: 0 10px 24px rgba(0,0,0,.25);
    text-transform: uppercase;
  }
  .card-art { position: absolute; inset: 0; width: 100%; height: 100%; }

  /* front */
  .front-brand {
    position: absolute; left: 0; right: 0; top: 118px;
    display: flex; flex-direction: column; align-items: center;
  }
  .brand-name {
    font-weight: 700; color: var(--brand-red);
    font-size: 56px; line-height: 1; letter-spacing: 1px;
  }
  .tagline {
    font-weight: 500; color: var(--brand-green);
    font-size: 14px; letter-spacing: 1px; margin-top: 4px;
  }
  .laser-rule {
    display: flex; align-items: center; margin-top: 6px;
  }
  .laser-rule .beam { width: 300px; height: 2px; background: var(--laser-blue); }
  .laser-rule .dot {
    width: 12px; height: 12px; border-radius: 50%; background: var(--laser-blue);
  }

  /* back */
  .back-details {
    position: absolute; left: 200px; right: 14px; top: 54px;
    display: flex; flex-direction: column; align-items: center; text-align: center;
  }
  .back-details .brand-name { font-size: 32px; }
  .quote-call {
    font-weight: 700; font-size: 26px; margin-top: 14px; letter-spacing: .5px;
  }
  .quote-call .red { color: var(--brand-red); }
  .quote-call .green { color: var(--brand-green); }
  .back-details .laser-rule { margin-top: 4px; }
  .back-details .laser-rule .beam { width: 220px; }
  .contact-name {
    font-weight: 500; color: var(--brand-green); font-size: 20px; margin-top: 14px;
  }
  .contact-line {
    font-weight: 500; font-size: 16px; margin-top: 6px; color: var(--brand-green);
  }
  .contact-line .label { color: var(--brand-red); margin-right: 4px; }
  .contact-line.email { font-size: 13px; }
</style>
</head>
<body>
<main class="sheet">

  <section class="card card-front">
    <svg class="card-art" viewBox="0 0 540 328" preserveAspectRatio="none">
      <defs>
        <linearGradient id="grass" x1="0" y1="0" x2="1" y2="1">
          <stop offset="0" stop-color="var(--grass-light)"/>
          <stop offset="1" stop-color="var(--grass-dark)"/>
        </linearGradient>
      </defs>
      <rect width="540" height="328" fill="url(#grass)" role="img" aria-label="Close-up photo of freshly mown green lawn"/>
      <polygon fill="var(--card-black)" points="0,112 30,100 58,118 92,96 120,110 150,92 186,116 214,100 250,104 282,90 310,114 346,98 380,108 410,94 446,116 478,100 510,110 540,98 540,236 506,248 474,228 442,246 408,224 376,240 340,222 306,246 272,230 240,244 206,226 170,242 138,222 104,246 72,228 38,244 0,226"/>
    </svg>
    <div class="front-brand">
      <div class="brand-name">Tidal Verge</div>
      <div class="tagline">For your professional cut lawns</div>
      <div class="laser-rule"><span class="beam"></span><span class="dot"></span></div>
    </div>
  </section>

  <section class="card card-back">
    <svg class="card-art" viewBox="0 0 540 328" preserveAspectRatio="none">
      <defs>
        <linearGradient id="grass-back" x1="0" y1="0" x2="1" y2="1">
          <stop offset="0" stop-color="var(--grass-light)"/>
          <stop offset="1" stop-color="var(--grass-dark)"/>
        </linearGradient>
        <linearGradient id="photo-fill" x1="0" y1="0" x2="1" y2="1">
          <stop offset="0" stop-color="var(--photo-tone-a)"/>
          <stop offset="1" stop-color="var(--photo-tone-b)"/>
        </linearGradient>
      </defs>
      <polygon fill="url(#grass-back)" role="img" aria-label="Strip of green lawn photo" points="360,0 540,0 540,64 520,52 500,70 476,46 452,60 430,34 404,48 384,20"/>
      <polygon fill="url(#photo-fill)" role="img" aria-label="Photo of a worker mowing a lawn on a ride-on mower" points="0,0 168,0 180,30 164,62 186,96 170,130 192,170 174,206 190,240 172,276 188,328 0,328"/>
    </svg>
    <div class="back-details">
      <div class="brand-name">Tidal Verge</div>
      <div class="quote-call"><span class="red">“Call for</span> <span class="green">free quote”</span></div>
      <div class="laser-rule"><span class="beam"></span><span class="dot"></span></div>
      <div class="contact-name">Darren Quellby</div>
      <div class="contact-line"><span class="label">P:</span>0413562049</div>
      <div class="contact-line email"><span class="label">E:</span>norma.vance@fernmail.com.au</div>
    </div>
  </section>

</main>
</body>
</html>
```